Fast growing Tech company needs redesign of Varnith's end user website!

We need to have our login screen, the dashboard, and the one page of the Varnith site to be redesigned for the end-users. Varnith is a document hosting service for title companies and real estate law firms. This allows the buyers and sellers to view their closing documents after closing along with many other features that help them out during the closing of their property. More information about what we do can be found on our test site https://qpx.482.sampledrafthost.example/. PLEASE NOTE: THE ABOVE SITE IS NOT THE ONE WE NEED REDONE. The above site is our corporate site that explains our service offering and we thought it would be helpful in providing you a better understanding of our service.
The site that we want to have redesigned is for the end user. THE SITE THAT NEEDS TO BE REDONE ARE THE SCREENSHOTS ATTACHED. We will need the login screen, dashboard, and the one page redesigned.
.
We will just need this in HTML and we will then do the rest for the placeholders for logos, data, mapping etc.
Overall, we want a new, fresh, and modern look for the website and we want the login screen, dashboard and one page website to be consistent in design. Again, these are the three screenshots that are attached.
For the winner, we will most likely need to hire you again for more sites because we have other versions.
Thank you and if any questions, please let us know.
Target Market(s)
This site is for buyer and sellers during the closing process of real estate transaction.

```html
<!DOCTYPE html>
<html lang="en">
<head>
<meta charset="utf-8">
<title>Varnith – Login</title>
<link href="https://fonts.googleapis.com/css2?family=Poppins:wght@400;500;600;700&display=swap" rel="stylesheet">
<style>
  :root {
    --brand-blue: #0f75bc;
    --white: #ffffff;
    --ink: #3f3f3f;
    --ink-soft: #5a5a5a;
    --field-bg: #f3f4f6;
    --button-bg: #474747;
    --link-blue: #3a86c8;
  }
  * { box-sizing: border-box; margin: 0; padding: 0; }
  html, body {
    width: 1200px; height: 800px; overflow: hidden;
    font-family: "Poppins", sans-serif;
    background: var(--white);
  }
  .page { position: relative; width: 1200px; height: 800px; }

  /* Brand panel */
  .brand-panel {
    position: absolute; left: 0; top: 0; width: 584px; height: 800px;
    background: var(--brand-blue); color: var(--white);
  }
  .brand-name {
    position: absolute; left: 88px; top: 34px;
    font-size: 38px; font-weight: 500; letter-spacing: 0.5px; line-height: 1;
  }
  .brand-title {
    position: absolute; left: 86px; top: 346px;
    font-size: 48px; font-weight: 400; line-height: 1.1;
  }
  .brand-title strong { font-weight: 700; }
  .brand-intro {
    position: absolute; left: 87px; top: 417px; width: 440px;
    font-size: 22px; font-weight: 400; line-height: 31px;
  }
  .copyright {
    position: absolute; left: 88px; top: 748px;
    font-size: 14px; font-weight: 600;
  }

  /* Top navigation */
  .top-nav {
    position: absolute; top: 48px; right: 0; left: 584px; height: 30px;
  }
  .nav-links {
    position: absolute; left: 232px; top: 0;
    font-size: 16px; color: var(--ink); font-weight: 400;
  }
  .nav-links .divider { margin: 0 4px; font-size: 18px; }
  .nav-login {
    position: absolute; left: 482px; top: 0;
    font-size: 16px; font-weight: 600; color: var(--link-blue);
    padding-bottom: 3px; border-bottom: 2px solid var(--link-blue);
    text-decoration: none;
  }

  /* Login form */
  .login-heading {
    position: absolute; left: 694px; top: 254px;
    font-size: 35px; font-weight: 400; color: var(--ink); line-height: 1.2;
  }
  .login-heading strong { font-weight: 700; }
  .signup-prompt {
    position: absolute; left: 698px; top: 309px;
    font-size: 18px; color: var(--ink-soft);
  }
  .signup-prompt a { color: var(--ink-soft); font-weight: 500; text-decoration: underline; text-underline-offset: 4px; }

  .field-label {
    position: absolute; left: 695px;
    font-size: 16px; font-weight: 600; color: var(--ink);
  }
  .label-email { top: 372px; }
  .label-password { top: 462px; }
  .field {
    position: absolute; left: 696px; width: 378px; height: 49px;
    background: var(--field-bg); border: none;
    padding: 0 20px; font-family: "Poppins", sans-serif; font-size: 14px; color: var(--ink);
  }
  .field::placeholder { color: #555; }
  .field-email { top: 398px; }
  .field-password { top: 488px; font-size: 18px; letter-spacing: 2px; }

  .submit-button {
    position: absolute; left: 696px; top: 562px; width: 378px; height: 49px;
    background: var(--button-bg); color: var(--white); border: none;
    font-family: "Poppins", sans-serif; font-size: 20px; font-weight: 600; letter-spacing: 1px;
  }
  .submit-icon { position: absolute; right: 24px; top: 16px; }
</style>
</head>
<body>
<main class="page">
  <section class="brand-panel">
    <div class="brand-name">varnith</div>
    <h1 class="brand-title">Login to <strong>Varnith</strong></h1>
    <p class="brand-intro">Log In with your data that you entered during your registration.</p>
    <p class="copyright">Copyright 2021 &nbsp;|&nbsp; All Rights Reserved</p>
  </section>

  <nav class="top-nav">
    <span class="nav-links">New User <span class="divider">/</span> Account Reset</span>
    <a class="nav-login" href="#">Login</a>
  </nav>

  <h2 class="login-heading">Login to <strong>your Account</strong></h2>
  <p class="signup-prompt">Don't have an account? <a href="#">Signup here</a></p>

  <label class="field-label label-email" for="email">Email*</label>
  <input class="field field-email" id="email" type="text" placeholder="USBKey or Certificate Number">

  <label class="field-label label-password" for="password">Password*</label>
  <input class="field field-password" id="password" type="text" value="**********">

  <button class="submit-button" type="button">SUBMIT
    <svg class="submit-icon" width="18" height="16" viewBox="0 0 18 16" aria-hidden="true">
      <path d="M0 8 L18 0 L14 16 L8 11 L15 3 L6 10 Z" fill="#ffffff"/>
    </svg>
  </button>
</main>
</body>
</html>
```